Specialist Medical practice after professional trifold flyer design for patient information brochure

I am the Director of the Kestrel Ridge Clinic, a specialist medial and surgical practice in Australia. I am after a professional design of a patient information trifold flyer that can be used for web distribution or for commercial printing for upcoming educational event. The design would need to allow change of images and text to be used as template for future topics but have a common brand look across them. Colours would follow the logo, but primarily blue colours for the kestrelridge theme. The inside text needs to be clearly contrasted to the background for easy reading, as often elderly patients. The design would make use of curves or circles, but open for hexagonal, triangle square vector components. I have included an outline for the initial brochure and included images to include. Other stock background images can be used if they increase the impact of the design over included. A winning design is also one that could be modified to a 4 page bi-fold brochure

Target Market(s)

This will be provided to patients in GP practices, podiatry clinics, radiological practices. Aimed at patients to read and be compelled to look to site or get consultation with me

Industry/Entity Type

Medical

Font styles to use
Serif
Sans Serif

Colors
33a6d7
0355a3
86cfc6
cedeed
0292cd
85cae6

Requirements
Must have
• The front cover needs to engage the patient to pick up and read- yes I have a painful ankle and want to find out more. the goal for the inside is to provide the options but be able to direct to website for more info - website currently undergoing upgrade. After professional modern look. Not bright contrasting colours like many advertising brochures. Needs to able to have images and text changed but following same look to create new topics
Nice to have
• The focus is a Tri-fold brochure. Nice to be able to modify to bifold. A winning design would even offer both, or submit separate bifold and trifold. I am open to different versions of similar look. (eg option of brochure with curved elements, triangular or square, or hexagonal.
Should not have
• To many contrasting colours. Text must be easily read on background, either white or coloured background texture with transparency

```html
<!DOCTYPE html>
<html lang="en">
<head>
<meta charset="utf-8">
<title>Ankle arthritis – Kestrel Ridge Clinic</title>
<link rel="stylesheet" href="https://fonts.googleapis.com/css2?family=PT+Sans:wght@400;700&display=swap">
<style>
  :root {
    --ink-bg: #000000;
    --brand-blue: #0a5aa8;
    --text-light: #ffffff;
    --xray-light: #cfcfcf;
    --xray-mid: #6e6e6e;
    --xray-dark: #1c1c1c;
  }
  html, body {
    margin: 0;
    padding: 0;
    width: 848px;
    height: 1200px;
    overflow: hidden;
    background: var(--ink-bg);
  }
  .panel {
    position: relative;
    width: 848px;
    height: 1200px;
    background: var(--ink-bg);
    color: var(--text-light);
    font-family: "PT Sans", sans-serif;
    overflow: hidden;
  }
  .radiograph { position: absolute; }
  .radiograph--lateral-ankle {
    left: 40px; top: 96px; width: 360px; height: 410px;
    background:
      radial-gradient(ellipse 55% 40% at 30% 78%, var(--xray-light) 0%, var(--xray-mid) 45%, transparent 80%),
      radial-gradient(ellipse 22% 60% at 38% 20%, #8a8a8a 0%, #3a3a3a 60%, transparent 90%),
      var(--xray-dark);
    -webkit-mask-image: linear-gradient(90deg, #000 0%, #000 45%, rgba(0,0,0,0.25) 62%, transparent 80%);
    mask-image: linear-gradient(90deg, #000 0%, #000 45%, rgba(0,0,0,0.25) 62%, transparent 80%);
  }
  .radiograph--fusion {
    left: 426px; top: 526px; width: 422px; height: 614px;
    background:
      radial-gradient(ellipse 65% 35% at 55% 82%, var(--xray-light) 0%, #9a9a9a 45%, transparent 85%),
      radial-gradient(ellipse 25% 45% at 72% 30%, #b5b5b5 0%, #5a5a5a 60%, transparent 95%),
      linear-gradient(180deg, #2a2a2a 0%, #3c3c3c 45%, #8a8a8a 100%);
    clip-path: polygon(180px 0, 422px 0, 422px 614px, 0 614px, 0 336px, 130px 336px, 130px 180px, 180px 180px);
  }
  .title-band {
    position: absolute;
    left: 0;
    margin: 0;
    background: var(--brand-blue);
    display: flex;
    align-items: center;
    font-weight: 700;
    font-size: 29px;
    color: var(--text-light);
    box-sizing: border-box;
  }
  .title-band--arthritis { top: 34px; width: 478px; height: 64px; justify-content: center; padding-left: 190px; }
  .title-band--fusion { top: 862px; width: 424px; height: 64px; padding-left: 50px; }
  .line {
    position: absolute;
    height: 25.6px;
    line-height: 25.6px;
    font-size: 22px;
    white-space: nowrap;
    text-align: justify;
    text-align-last: justify;
  }
  .line--end { text-align-last: left; }
</style>
</head>
<body>
<main class="panel">
  <div class="radiograph radiograph--lateral-ankle" role="img" aria-label="Lateral x-ray of an arthritic ankle"></div>
  <div class="radiograph radiograph--fusion" role="img" aria-label="Lateral x-ray of an ankle fused with plate and screws"></div>

  <h1 class="title-band title-band--arthritis">Ankle arthritis</h1>

  <section class="intro">
    <div class="line" style="left:238px;top:107px;width:560px">Ankle arthritis is a painful condition where there is loss</div>
    <div class="line" style="left:242px;top:133px;width:556px">of cartilage from the ankle joint surface. Although not</div>
    <div class="line" style="left:246px;top:158px;width:552px">as common as knee or hip arthritis, pain can be</div>
    <div class="line line--end" style="left:253px;top:184px;width:545px">debilitating affecting quality of life.</div>
    <div class="line" style="left:256px;top:210px;width:542px">Arthritis of the joint can be caused by trauma joint</div>
    <div class="line" style="left:260px;top:235px;width:538px">such as fracture or recurrent instability or secondary</div>
    <div class="line" style="left:263px;top:261px;width:535px">from inflammatory conditions such as rheumatoid</div>
    <div class="line line--end" style="left:288px;top:286px;width:510px">arthritis.</div>
    <div class="line" style="left:318px;top:312px;width:480px">Pain from the joint will occur with activity</div>
    <div class="line" style="left:343px;top:338px;width:455px">causing a limp, limiting walking speed and</div>
    <div class="line" style="left:360px;top:363px;width:438px">distance.&nbsp; Often there is swelling of the joint</div>
    <div class="line line--end" style="left:400px;top:389px;width:398px">with progressive loss of motion.</div>
    <div class="line" style="left:413px;top:414px;width:385px">Diagnosis is made with examination of</div>
    <div class="line" style="left:411px;top:440px;width:387px">the ankle and weight bearing x-rays</div>
    <div class="line line--end" style="left:411px;top:466px;width:387px">showing loss of joint space.</div>
  </section>

  <section class="treatment">
    <div class="line" style="left:50px;top:523px;width:552px">When pain medication, activity modification and shoe</div>
    <div class="line" style="left:50px;top:549px;width:550px">ware modification is no longer effective to control the</div>
    <div class="line" style="left:50px;top:574px;width:550px">pain then then it is worthwhile discussing with your GP</div>
    <div class="line" style="left:50px;top:600px;width:548px">for referral to Dr Marcus Elvery for an opinion on</div>
    <div class="line" style="left:50px;top:626px;width:548px">further treatment.&nbsp; As an Orthopaedic Foot and Ankle</div>
    <div class="line" style="left:50px;top:651px;width:544px">surgeon, he will be able to assess your conditions and</div>
    <div class="line line--end" style="left:50px;top:677px;width:544px">give advice on the best options for your treatment.</div>
    <div class="line" style="left:50px;top:702px;width:524px">The decision on the best option is based on your</div>
    <div class="line" style="left:50px;top:728px;width:516px">age, activity level, existing medical problems,</div>
    <div class="line" style="left:50px;top:754px;width:510px">previous ankle treatment and your expected</div>
    <div class="line" style="left:50px;top:779px;width:503px">outcome from treatment.&nbsp; In the situation of end</div>
    <div class="line" style="left:50px;top:805px;width:489px">stage arthritis options consist of either Ankle</div>
    <div class="line line--end" style="left:50px;top:830px;width:489px">fusion or Total Ankle replacement.</div>
  </section>

  <h2 class="title-band title-band--fusion">Ankle Fusion Surgery</h2>

  <section class="fusion">
    <div class="line" style="left:50px;top:935px;width:356px">This operation aims to stiffen the</div>
    <div class="line" style="left:50px;top:961px;width:356px">ankle joint by fusing the tibia and</div>
    <div class="line" style="left:50px;top:986px;width:356px">talus together in the optimal</div>
    <div class="line" style="left:50px;top:1012px;width:356px">position for function.&nbsp; The common</div>
    <div class="line" style="left:50px;top:1038px;width:356px">thought is that there will be no</div>
    <div class="line" style="left:50px;top:1063px;width:356px">movement of the foot, and the</div>
    <div class="line" style="left:50px;top:1089px;width:356px">patient will walk with a limp.&nbsp; The</div>
    <div class="line" style="left:50px;top:1114px;width:356px">fusion only occurs at the ankle joint,</div>
  </section>
</main>
</body>
</html>
```